10 Page Marketing Report Template - Quillmont Care Associates

https://www.vexaclip.com/view/8f1d2e7b90c44a6f81e2d3b5c7a9f014

We are creating a professional, modern, and slightly edgy PDF-style report document (about 10 pages) to showcase the results of a client’s first 30 days with Quillmont Care Associates.

The report will be designed as a customizable Canva template so the Client Success team can easily update logos, screenshots, and text for each client.

This document will serve as both a visual presentation piece and a report deliverable, blending clean design, modern layout, and data-driven storytelling.

I am attaching the content for the report doc and the design brief along with the logo.
Here is our website for design style, look, and feel: https://quillmontcare.example/

Here is a quick overview video I made:

```html
<!DOCTYPE html>
<html lang="en">
<head>
<meta charset="utf-8">
<title>30 Days to Value Report – Quillmont Care Associates</title>
<link href="https://fonts.googleapis.com/css2?family=Montserrat:wght@400;500;600;700;800&family=Lato:wght@400;700&display=swap" rel="stylesheet">
<style>
:root{
  --backdrop:#a9a9a9;
  --paper:#ffffff;
  --navy:#1f2a4e;
  --navy-deep:#161d3f;
  --gold:#fcb100;
  --ink:#3c4052;
  --muted:#9a9ea8;
  --rule:#c9ccd3;
}
*{box-sizing:border-box;margin:0;padding:0}
html,body{width:1200px;height:1048px;overflow:hidden;background:var(--backdrop)}
body{position:relative;font-family:"Lato",sans-serif;color:var(--ink)}
.page{position:absolute;width:361px;height:467px;background:var(--paper);box-shadow:2px 3px 6px rgba(0,0,0,.25);overflow:hidden}
.abs{position:absolute}
.p1{left:37px;top:44px}.p2{left:422px;top:44px}.p3{left:806px;top:44px}
.p4{left:223px;top:538px}.p5{left:606px;top:538px}

/* name mark: one colour, one weight, with a plain square */
.brand{position:absolute;display:flex;align-items:center;gap:4px;font-family:"Lato",sans-serif;font-weight:700;color:var(--navy);white-space:nowrap;line-height:1}
.brand::before{content:"";display:block;background:var(--navy)}
.brand-sm{right:22px;top:20px;font-size:6.5px}
.brand-sm::before{width:6px;height:6px}
.header-rule{position:absolute;left:22px;top:31px;width:241px;height:2px;background:var(--navy)}

.heading{position:absolute;left:22px;top:53px;font-family:"Montserrat",sans-serif;font-weight:700;font-size:10px;line-height:1.15;color:var(--navy)}
.heading span{display:block;color:var(--gold)}
.body{font-size:6px;line-height:1.45;color:var(--ink)}
.subhead{position:absolute;left:22px;font-family:"Montserrat",sans-serif;font-weight:700;font-size:9.5px;color:var(--navy)}

.footer{position:absolute;left:22px;top:433px;width:317px;height:12px}
.footer-tag{position:absolute;left:0;top:0;width:97px;height:12px;background:var(--navy);color:#fff;font-family:"Montserrat",sans-serif;font-weight:600;font-size:5.5px;line-height:12px;padding-left:5px}
.footer-line{position:absolute;left:97px;top:6px;width:208px;height:1px;background:var(--rule)}
.footer-num{position:absolute;right:0;top:2px;font-family:"Montserrat",sans-serif;font-weight:700;font-size:6px;color:var(--navy)}

/* cover */
.cover-logo-box{left:111px;top:28px;width:75px;height:45px;border:1px solid #777;font-family:"Montserrat",sans-serif;font-weight:500;font-size:9px;line-height:1.2;color:#222;padding:9px 0 0 12px}
.cover-brand{left:200px;top:46px;font-size:10.5px}
.cover-brand::before{width:9px;height:9px}
.cover-title{left:111px;top:176px;font-family:"Montserrat",sans-serif;font-weight:400;font-size:27px;color:var(--navy);line-height:1.2}
.cover-title strong{display:block;color:var(--gold);font-weight:800;font-size:28px}
.cover-sub{left:111px;top:254px;border-left:2px solid var(--gold);padding-left:8px;font-size:12px;line-height:1.25;color:var(--navy)}
.cover-meta{left:111px;font-size:9px;font-weight:700;color:var(--navy)}

/* highlights */
.win{position:absolute;font-size:5.5px;line-height:1.45;color:var(--ink);width:66px}
.win-icon{position:absolute;width:24px;height:22px}

/* audits */
.audit-bar{position:absolute;color:#fff;font-size:6px;display:flex;align-items:center;justify-content:center;text-align:center;line-height:1.25}
.audit-note{position:absolute;font-size:5.5px;line-height:1.45;text-align:center;width:92px;color:var(--ink)}

/* website */
.opt-label{position:absolute;font-size:6px;line-height:1.4;text-align:center;width:80px;color:var(--ink)}
.screen{position:absolute;background:#2f3e66;color:#fff;font-family:"Montserrat",sans-serif;font-weight:700;text-align:center;display:flex;align-items:center;justify-content:center;line-height:1.2}
</style>
</head>
<body>

<!-- Cover -->
<section class="page p1">
  <svg class="abs" style="left:0;top:0" width="361" height="467" aria-hidden="true">
    <rect x="0" y="0" width="64" height="467" fill="#1c2446"/>
    <polygon points="64,0 87,0 87,143 64,167" fill="var(--gold)"/>
    <polygon points="64,298 87,322 87,467 64,467" fill="var(--gold)"/>
  </svg>
  <div class="abs cover-logo-box">Client logo<br>placeholder</div>
  <div class="brand cover-brand">Quillmont Care Associates</div>
  <h1 class="abs cover-title">30 DAYS TO<strong>VALUE REPORT</strong></h1>
  <p class="abs cover-sub">Your First Month<br>Of Progress</p>
  <p class="abs cover-meta" style="top:381px">Client Name:</p>
  <p class="abs cover-meta" style="top:408px">Date:</p>
  <p class="abs cover-meta" style="top:435px">Prepared by: Quillmont Care Associates</p>
</section>

<!-- Welcome -->
<section class="page p2">
  <div class="header-rule"></div>
  <div class="brand brand-sm">Quillmont Care Associates</div>
  <h2 class="heading">Welcome &amp;<span>Overview</span></h2>
  <p class="abs body" style="left:22px;top:90px;width:318px">The first 30 days are about creating momentum. Our goal was to build the foundation for measurable growth — from your website and Searchly Business Profile to your SEO systems, audits, and backlink strategy.</p>
  <p class="abs body" style="left:22px;top:114px;width:318px">This report highlights what's been accomplished and what's next in your marketing journey</p>
  <div class="abs" style="left:22px;top:148px;width:317px;height:260px;background:var(--gold)"></div>
  <div class="abs" role="img" aria-label="Photo of three colleagues shaking hands in a bright office" style="left:22px;top:153px;width:317px;height:249px;background:linear-gradient(135deg,#c8dbe6 0%,#8aa5b6 45%,#4b5a68 100%)"></div>
  <div class="footer"><div class="footer-tag">Placeholder for client logo</div><div class="footer-line"></div><div class="footer-num">02</div></div>
</section>

<!-- Highlights -->
<section class="page p3">
  <div class="header-rule"></div>
  <div class="brand brand-sm">Quillmont Care Associates</div>
  <h2 class="heading">Highlights &amp;<span>Quick Wins</span></h2>
  <div class="abs" role="img" aria-label="Small rocket launch icon" style="left:190px;top:70px;width:24px;height:42px;border:1px solid var(--muted);border-radius:12px 12px 3px 3px"></div>
  <svg class="abs" style="left:0;top:0" width="361" height="467" aria-hidden="true" fill="none">
    <path d="M202 118 C202 135 190 140 175 140 L53 140" stroke="var(--muted)" stroke-width="1"/>
    <path d="M53 140 A29.5 29.5 0 0 0 53 199" stroke="var(--gold)" stroke-width="2.5"/>
    <path d="M53 199 L307 199" stroke="var(--muted)" stroke-width="1"/>
    <path d="M307 199 A29 29 0 0 1 307 257" stroke="#b5b5b5" stroke-width="2.5"/>
    <path d="M307 257 L53 257" stroke="var(--muted)" stroke-width="1"/>
    <path d="M53 257 A29 29 0 0 0 53 315" stroke="var(--navy-deep)" stroke-width="2.5"/>
    <path d="M53 315 L307 315" stroke="var(--muted)" stroke-width="1"/>
    <path d="M307 315 A29 29 0 0 1 307 373" stroke="var(--gold)" stroke-width="2.5"/>
    <path d="M307 373 L178 373 C165 373 158 382 158 405" stroke="var(--muted)" stroke-width="1"/>
    <circle cx="158" cy="405" r="3" fill="var(--navy)"/>
  </svg>
  <svg class="win-icon" style="left:149px;top:159px" viewBox="0 0 24 22" fill="none" stroke="var(--navy)" stroke-width="1" aria-hidden="true"><rect x="1" y="1" width="22" height="16"/><line x1="1" y1="5" x2="23" y2="5"/><rect x="7" y="10" width="10" height="8" fill="#fff"/></svg>
  <p class="win" style="left:180px;top:162px">Website launched and optimized for SEO</p>
  <svg class="win-icon" style="left:73px;top:217px" viewBox="0 0 24 22" fill="none" stroke="var(--navy)" stroke-width="1" aria-hidden="true"><rect x="1" y="1" width="20" height="16"/><circle cx="12" cy="11" r="6" fill="#fff"/><line x1="16" y1="15" x2="21" y2="20"/></svg>
  <p class="win" style="left:108px;top:220px">Comprehensive SEO audits completed</p>
  <svg class="win-icon" style="left:212px;top:217px" viewBox="0 0 24 22" fill="none" stroke="var(--navy)" stroke-width="1" aria-hidden="true"><rect x="1" y="1" width="22" height="20"/><circle cx="12" cy="8" r="3"/><rect x="5" y="15" width="5" height="3"/><rect x="14" y="15" width="5" height="3"/></svg>
  <p class="win" style="left:246px;top:220px">Searchly Business Profiles verified and optimized</p>
  <svg class="win-icon" style="left:73px;top:275px" viewBox="0 0 24 22" fill="none" stroke="var(--navy)" stroke-width="1" aria-hidden="true"><rect x="1" y="1" width="20" height="17"/><line x1="4" y1="9" x2="18" y2="9"/><line x1="4" y1="12" x2="18" y2="12"/><line x1="4" y1="15" x2="14" y2="15"/><line x1="8" y1="18" x2="8" y2="21"/></svg>
  <p class="win" style="left:108px;top:278px;width:50px">First blog articles published</p>
  <svg class="win-icon" style="left:212px;top:275px" viewBox="0 0 24 22" fill="none" stroke="var(--navy)" stroke-width="1" aria-hidden="true"><rect x="1" y="5" width="16" height="16"/><rect x="7" y="1" width="16" height="14" fill="#fff"/><path d="M9 15 L15 9"/></svg>
  <p class="win" style="left:246px;top:278px;width:76px">Backlink strategy implementation underway</p>
  <svg class="win-icon" style="left:212px;top:334px" viewBox="0 0 24 22" fill="none" stroke="var(--navy)" stroke-width="1" aria-hidden="true"><rect x="1" y="1" width="22" height="15"/><line x1="12" y1="16" x2="12" y2="20"/><line x1="7" y1="20" x2="17" y2="20"/><path d="M6 12 V9 M10 12 V6 M14 12 V8 M18 12 V4"/></svg>
  <p class="win" style="left:246px;top:338px">Tracking and analytics systems connected</p>
  <div class="footer"><div class="footer-tag">Placeholder for client logo</div><div class="footer-line"></div><div class="footer-num">03</div></div>
</section>

<!-- Audits -->
<section class="page p4">
  <div class="header-rule"></div>
  <div class="brand brand-sm">Quillmont Care Associates</div>
  <h2 class="heading">Comprehensive Audits<span>&amp; Strategy Development</span></h2>
  <p class="abs body" style="left:22px;top:89px;width:318px">To ensure long-term results, our team conducted a full suite of technical and strategic audits during the first month. These insights guided your SEO roadmap and content strategy moving forward.</p>
  <h3 class="subhead" style="top:123px">Audits &amp; Deliverables Completed:</h3>
  <svg class="abs" style="left:0;top:0" width="361" height="467" fill="none" stroke="#9aa0ad" stroke-width=".6" aria-hidden="true">
    <path d="M213 186 L220 196 L316 196" stroke-dasharray="2 1.5"/><circle cx="213" cy="186" r="2" fill="#4a62d8" stroke="none"/>
    <path d="M199 220 L206 230 L309 230" stroke-dasharray="2 1.5"/><circle cx="199" cy="220" r="2" fill="#4a62d8" stroke="none"/>
    <path d="M186 252 L193 262 L309 262" stroke-dasharray="2 1.5"/><circle cx="186" cy="252" r="2" fill="#4a62d8" stroke="none"/>
    <path d="M174 285 L181 295 L307 295" stroke-dasharray="2 1.5"/><circle cx="174" cy="285" r="2" fill="#4a62d8" stroke="none"/>
    <path d="M162 317 L169 327 L305 327" stroke-dasharray="2 1.5"/><circle cx="162" cy="317" r="2" fill="#4a62d8" stroke="none"/>
    <path d="M149 357 L156 367 L272 367" stroke-dasharray="2 1.5"/>
  </svg>
  <div class="audit-bar" style="left:22px;top:174px;width:191px;height:22px;background:#161d3f">Technical SEO Audit</div>
  <div class="audit-bar" style="left:35px;top:208px;width:164px;height:21px;background:#1f2a5c">Backlink Audit</div>
  <div class="audit-bar" style="left:51px;top:240px;width:135px;height:21px;background:#2b3a80">Competitor Analysis</div>
  <div class="audit-bar" style="left:63px;top:273px;width:111px;height:21px;background:#3347a0">On-Page SEO Audit</div>
  <div class="audit-bar" style="left:75px;top:305px;width:87px;height:21px;background:#3d55c2">Content Audit</div>
  <div class="audit-bar" style="left:90px;top:337px;width:59px;height:31px;background:#4a62d8">Strategy<br>Development</div>
  <p class="audit-note" style="left:224px;top:178px;width:76px">Site health, indexation, and crawl efficiency</p>
  <p class="audit-note" style="left:210px;top:212px">Link quality, toxicity review, and authority scoring</p>
  <p class="audit-note" style="left:197px;top:245px">Top-ranking competitors' content, backlinks, and keyword profiles</p>
  <p class="audit-note" style="left:185px;top:277px;width:104px">Metadata, headings, internal links, and content structure</p>
  <p class="audit-note" style="left:174px;top:309px">Keyword targeting, topical gaps, and conversion opportunities</p>
  <p class="audit-note" style="left:162px;top:350px;width:86px">90-day SEO plan and keyword roadmap created</p>
  <div class="footer"><div class="footer-tag">Placeholder for client logo</div><div class="footer-line"></div><div class="footer-num">04</div></div>
</section>

<!-- Website -->
<section class="page p5">
  <div class="header-rule"></div>
  <div class="brand brand-sm">Quillmont Care Associates</div>
  <h2 class="heading">Website<span>Progress</span></h2>
  <h3 class="subhead" style="top:87px">Launched Pages</h3>
  <p class="abs body" style="left:22px;top:111px;width:320px">List live pages <span style="color:var(--gold)">⟶</span>&nbsp;&nbsp;&nbsp; • Home, &nbsp;&nbsp;&nbsp; • About, &nbsp;&nbsp;&nbsp; • Services, &nbsp;&nbsp;&nbsp; • Contact &nbsp;&nbsp;&nbsp;&nbsp; • etc.</p>
  <h3 class="subhead" style="top:137px">Optimizations Completed</h3>
  <svg class="abs" style="left:0;top:0" width="361" height="467" fill="none" aria-hidden="true">
    <line x1="22" y1="180" x2="338" y2="180" stroke="#6b6f7a" stroke-width="2.5"/>
    <g stroke="var(--gold)" stroke-width=".8" stroke-dasharray="1.5 1.5">
      <line x1="53" y1="193" x2="53" y2="218"/><line x1="131" y1="193" x2="131" y2="218"/>
      <line x1="205" y1="193" x2="205" y2="218"/><line x1="298" y1="193" x2="298" y2="218"/>
    </g>
    <g fill="#fff" stroke="var(--navy)" stroke-width="1.2">
      <circle cx="53" cy="180" r="13"/><circle cx="131" cy="180" r="13"/>
      <circle cx="205" cy="180" r="13"/><circle cx="298" cy="180" r="13"/>
    </g>
    <g stroke="var(--navy)" stroke-width=".8">
      <circle cx="51" cy="178" r="5"/><line x1="55" y1="182" x2="59" y2="186"/>
      <rect x="127" y="176" width="8" height="8"/><path d="M131 172 V176 M131 184 V188 M123 180 H127 M135 180 H139"/>
      <circle cx="205" cy="180" r="6"/><path d="M202 177 Q203 183 208 183 L208 181 L206 180"/>
      <rect x="294" y="172" width="8" height="15" rx="1"/><line x1="297" y1="184" x2="299" y2="184"/>
    </g>
  </svg>
  <p class="opt-label" style="left:13px;top:225px">On-page SEO<br>(titles, meta, H1s)</p>
  <p class="opt-label" style="left:91px;top:225px">Local schema<br>added</p>
  <p class="opt-label" style="left:167px;top:225px">Call tracking<br>integrated</p>
  <p class="opt-label" style="left:258px;top:225px">Mobile responsiveness<br>reviewed</p>
  <h3 class="subhead" style="top:255px">Next Steps</h3>
  <p class="abs body" style="left:22px;top:281px">• CRO improvements &nbsp;&nbsp;&nbsp; • Additional service or location pages</p>
  <div class="abs" style="left:38px;top:306px;width:121px;height:78px;background:#1b1f2b;border-radius:3px"></div>
  <div class="screen" style="left:42px;top:310px;width:113px;height:70px;font-size:10px">Image<br>Placeholder</div>
  <div class="abs" style="left:26px;top:384px;width:145px;height:4px;background:#b8bcc4;border-radius:0 0 3px 3px"></div>
  <div class="abs" style="left:234px;top:292px;width:53px;height:108px;background:#1b1f2b;border-radius:7px"></div>
  <div class="screen" style="left:237px;top:295px;width:47px;height:102px;border-radius:5px;font-size:6.5px">Image<br>Placeholder</div>
  <div class="footer"><div class="footer-tag">Placeholder for client logo</div><div class="footer-line"></div><div class="footer-num">05</div></div>
</section>

</body>
</html>
```